Your 'not so average' farmers. We are farmers and entrepreneurs trying to connect the great divide.

HBQ (Thornwick Provision Inc) is a family owned farm (in our 3rd generation). We grow vegetables (corn, soy, potatoes, snap beans) but we also invest in and grow businesses. These other businesses can be non-farming related businesses. We are family oriented, environmentally concise, and active in our small community. We need a business card to hand out to our fellow farmers, businesses we would like to partner with and invest in, and community members. So, we need a card with a natural, 'tenders of the land' feel for the farmers but no overly so that we seem centered on farming for the other businesses. We would like it to have our Company info (name, number, email, phone, fax) then Personal info for us five who run the joint (Name, phone, email). So we will order 100 cards for each 5 who work at HBQ (500total) that is professional, not boring or hokey, but catching and unique.
Target Market(s)
Farmers, Business Owners, Investors, Community Members
Industry/Entity Type
Farming
Contact Information for Business Card
Office info on one side:
Thornwick Provision Inc.
1187 Cedar Row
Pell Hollow, WI 54872
Office: (608) 555-0147
Fax: (608) 555-0183
thornwickoffice@fieldpostmail.example
Personal Info for the 5 who run HBQ. Everybody will have their own personal info on their cards(maybe on the other side):
Name
Mobile
Email
Look and feel

```html
<!DOCTYPE html>
<html lang="en">
<head>
<meta charset="utf-8">
<title>Thornwick Provision Inc. — Business Card</title>
<link rel="stylesheet" href="https://fonts.googleapis.com/css2?family=Montserrat:wght@700&family=Questrial&display=swap">
<style>
  :root {
    --bg: #ece8e1;
    --card: #ffffff;
    --green: #b2cf78;
    --cream: #f6f0b8;
    --brown: #5e3818;
    --olive: #a9a877;
    --shadow: rgba(60, 40, 20, 0.18);
  }
  * { box-sizing: border-box; margin: 0; padding: 0; }
  html, body {
    width: 1200px; height: 1000px; overflow: hidden;
    background: var(--bg);
    font-family: "Questrial", sans-serif;
    color: var(--brown);
  }
  .card {
    position: absolute; left: 220px;
    width: 760px; height: 434px;
    background: var(--card);
    border-radius: 40px;
    overflow: hidden;
    box-shadow: 0 10px 30px var(--shadow);
  }
  .card--front { top: 44px; }
  .card--back { top: 522px; }
  .card__bands { position: absolute; inset: 0; width: 100%; height: 100%; }
  .band--green { fill: var(--green); }
  .band--cream { fill: var(--cream); }

  .brand {
    position: absolute; display: flex; align-items: center; gap: 14px;
    font-family: "Montserrat", sans-serif; font-weight: 700;
    color: var(--brown); letter-spacing: 1px;
  }
  .brand__dot { border-radius: 50%; background: var(--olive); flex: none; }
  .card--front .brand { left: 0; right: 0; top: 140px; justify-content: center; font-size: 34px; }
  .card--front .brand__dot { width: 44px; height: 44px; }
  .card--back .brand { right: 40px; top: 88px; font-size: 15px; gap: 8px; }
  .card--back .brand__dot { width: 20px; height: 20px; }

  .holder-name {
    position: absolute; left: 40px; bottom: 34px;
    font-family: "Montserrat", sans-serif; font-weight: 700;
    font-size: 28px; letter-spacing: 0.5px;
  }
  .personal-contacts {
    position: absolute; right: 44px; bottom: 42px;
    display: flex; gap: 34px; font-size: 21px;
  }
  .contact { display: flex; align-items: center; gap: 9px; white-space: nowrap; }
  .icon { width: 20px; height: 20px; flex: none; fill: none; stroke: var(--cream); stroke-width: 1.8; stroke-linejoin: round; stroke-linecap: round; }
  .icon--solid { fill: var(--cream); stroke: none; }

  .company-name {
    position: absolute; left: 44px; top: 38px;
    font-family: "Montserrat", sans-serif; font-weight: 700;
    font-size: 33px; letter-spacing: 0.3px;
  }
  .office-contacts {
    position: absolute; left: 40px; bottom: 34px;
    display: flex; flex-direction: column; gap: 6px; font-size: 22px;
  }
  .address {
    position: absolute; right: 40px; bottom: 34px;
    display: flex; align-items: flex-start; gap: 10px;
    text-align: right; font-size: 22px; line-height: 1.3;
  }
  .address .icon { width: 24px; height: 28px; margin-top: 4px; }
</style>
</head>
<body>

<section class="card card--front" aria-label="Business card, personal side">
  <svg class="card__bands" viewBox="0 0 760 434" preserveAspectRatio="none" aria-hidden="true">
    <polygon class="band--cream" points="0,316 760,276 760,290 0,330"/>
    <polygon class="band--green" points="0,330 760,290 760,434 0,434"/>
  </svg>

  <div class="brand"><span class="brand__dot"></span>THORNWICK PROVISION</div>

  <div class="holder-name">NAME</div>

  <div class="personal-contacts">
    <span class="contact">
      <svg class="icon" viewBox="0 0 20 20" aria-hidden="true"><rect x="5" y="1.5" width="10" height="17" rx="2"/><line x1="9" y1="15.5" x2="11" y2="15.5"/></svg>
      12345678901
    </span>
    <span class="contact">
      <svg class="icon" viewBox="0 0 20 20" aria-hidden="true"><rect x="1.5" y="4" width="17" height="12" rx="1"/><polyline points="1.5,4 10,11 18.5,4"/></svg>
      youremail@fieldpostmail.example
    </span>
  </div>
</section>

<section class="card card--back" aria-label="Business card, company side">
  <svg class="card__bands" viewBox="0 0 760 434" preserveAspectRatio="none" aria-hidden="true">
    <polygon class="band--cream" points="0,146 760,296 760,310 0,160"/>
    <polygon class="band--green" points="0,160 760,310 760,434 0,434"/>
  </svg>

  <h1 class="company-name">THORNWICK PROVISION INC.</h1>
  <div class="brand"><span class="brand__dot"></span>THORNWICK PROVISION</div>

  <div class="office-contacts">
    <span class="contact">
      <svg class="icon icon--solid" viewBox="0 0 20 20" aria-hidden="true"><path d="M5 2l3 4-2 2c1 2.5 3.5 5 6 6l2-2 4 3-2 3C9 18 2 11 2 4z"/></svg>
      (608) 555-0147
    </span>
    <span class="contact">
      <svg class="icon" viewBox="0 0 20 20" aria-hidden="true"><rect x="5" y="2" width="10" height="6"/><rect x="2" y="8" width="16" height="9" rx="1"/><line x1="6" y1="13" x2="14" y2="13"/></svg>
      (608) 555-0183
    </span>
    <span class="contact">
      <svg class="icon" viewBox="0 0 20 20" aria-hidden="true"><rect x="1.5" y="4" width="17" height="12" rx="1"/><polyline points="1.5,4 10,11 18.5,4"/></svg>
      thornwickoffice@fieldpostmail.example
    </span>
  </div>

  <address class="address" style="font-style:normal">
    <span>1187 Cedar Row<br>Pell Hollow, WI 54872</span>
    <svg class="icon icon--solid" viewBox="0 0 20 24" aria-hidden="true"><path d="M10 1a8 8 0 0 0-8 8c0 6 8 14 8 14s8-8 8-14a8 8 0 0 0-8-8zm0 11a3 3 0 1 1 0-6 3 3 0 0 1 0 6z"/></svg>
  </address>
</section>

</body>
</html>
```